Informational Chiropractic Brochure

We need an informational bi-fold brochure. It needs to include information about chiropractic, helpful for back pain, neck pain, migraines, etc. These brochures will be handed out at corporate chair massage events to encourage people to go beyond a massage and seek chiropractic for their musculoskeletal issues.

Target Market(s)

Men and Women, ages 25 to 50, business women

Font styles to use
Serif
Sans Serif

Colors
f37122
0355a3
85acd3

Requirements
Must have
• The least invasive treatment for back pain relief

```html
<!DOCTYPE html>
<html lang="en">
<head>
<meta charset="utf-8">
<title>Spine Harbor Chiropractic – Bi-fold Brochure</title>
<link href="https://fonts.googleapis.com/css2?family=Cinzel:wght@400;600;700&family=Open+Sans:wght@400;600&display=swap" rel="stylesheet">
<style>
  :root{
    --navy:#1c3658;
    --navy-deep:#162c49;
    --blue:#0355a3;
    --sky:#85acd3;
    --gold:#e8a33a;
    --white:#ffffff;
    --ink:#33475f;
    --stage:#d9dadc;
  }
  *{box-sizing:border-box;margin:0;padding:0}
  html,body{width:804px;height:1200px;overflow:hidden;background:var(--stage)}
  body{position:relative;font-family:"Open Sans",Arial,sans-serif}
  .spread{position:absolute;left:22px;width:760px;height:520px;box-shadow:0 6px 18px rgba(0,0,0,.18);overflow:hidden;background:var(--white)}
  .spread--outer{top:50px}
  .spread--inner{top:630px}
  .spread svg.shapes{position:absolute;inset:0;width:760px;height:520px}
  .txt{position:absolute}
  .serif{font-family:"Cinzel",Georgia,serif}
  .heading{font-family:"Cinzel",Georgia,serif;font-weight:700;letter-spacing:.5px;text-transform:uppercase}
  .body-copy{font-size:9px;line-height:1.5}
  .on-dark{color:var(--white)}
  .on-light{color:var(--ink)}
  .accent{color:var(--gold)}

  /* outer spread */
  .intro{left:26px;top:168px;width:300px}
  .intro .heading{font-size:12px;color:var(--gold)}
  .intro .title{font-size:17px;color:var(--white);margin:4px 0 10px}
  .intro .body-copy{color:#c9d6e6}
  .hours{left:210px;top:395px;width:150px;text-align:right;font-size:9px;line-height:1.6;color:var(--white)}
  .address{left:26px;top:440px;width:200px;font-size:9px;line-height:1.6;color:#c9d6e6}
  .brand{left:590px;top:140px;display:flex;align-items:center;gap:8px}
  .brand-mark{width:20px;height:20px;border-radius:50%;background:var(--navy)}
  .brand-name{font-family:"Cinzel",Georgia,serif;font-weight:600;font-size:11px;line-height:1.2;color:var(--navy);width:110px}
  .tagline{left:400px;top:290px;width:220px;color:var(--white)}
  .tagline .big{font-family:"Cinzel",Georgia,serif;font-size:19px;font-weight:600}
  .tagline .big b{color:var(--gold)}
  .tagline .small{font-family:"Cinzel",Georgia,serif;font-size:12px;margin-top:2px}
  .phone{left:612px;top:470px;font-family:"Cinzel",Georgia,serif;font-weight:600;font-size:12px;color:var(--white)}

  /* inner spread */
  .policy{left:20px;width:200px}
  .policy .heading{font-size:14px;color:var(--navy);margin-bottom:6px}
  .policy--payment{top:28px}
  .policy--plans{top:312px}
  .policy--questions{top:400px}
  .brand--small{left:20px;top:488px}
  .brand--small .brand-mark{width:14px;height:14px}
  .brand--small .brand-name{font-size:8px;width:120px}
  .service-title{font-size:13px;color:var(--white)}
  .svc-spinal{left:450px;top:28px}
  .svc-myo{left:455px;top:190px}
  .svc-adjust{left:250px;top:388px;width:170px;line-height:1.25}
  .services{left:500px;top:400px;width:230px;text-align:center;color:var(--white)}
  .services .heading{font-size:16px;margin-bottom:6px}
  .services .body-copy{font-family:"Cinzel",Georgia,serif;font-size:10px;line-height:1.45}
</style>
</head>
<body>

<!-- OUTER SPREAD: back cover + front cover -->
<section class="spread spread--outer" aria-label="Brochure outside">
  <svg class="shapes" viewBox="0 0 760 520" aria-hidden="false">
    <defs>
      <linearGradient id="photoStaff" x1="0" y1="0" x2="1" y2="1">
        <stop offset="0" stop-color="#e9f0f7"/><stop offset="1" stop-color="#9fb9d4"/>
      </linearGradient>
      <linearGradient id="photoSpine" x1="0" y1="0" x2="1" y2="1">
        <stop offset="0" stop-color="#3a1a1a"/><stop offset=".6" stop-color="#8a2a1c"/><stop offset="1" stop-color="#2a1414"/>
      </linearGradient>
      <linearGradient id="photoSkin" x1="0" y1="0" x2="1" y2="1">
        <stop offset="0" stop-color="#efe2d8"/><stop offset="1" stop-color="#c9a993"/>
      </linearGradient>
    </defs>
    <!-- back cover panel -->
    <rect class="panel-back" x="0" y="0" width="380" height="520" fill="var(--navy)"/>
    <polygon points="0,20 252,20 215,142 0,142" fill="var(--sky)"/>
    <rect x="48" y="28" width="158" height="106" fill="url(#photoStaff)" role="img" aria-label="Photo of the clinic's smiling medical staff"/>
    <polygon points="256,20 372,20 336,142 218,142" fill="url(#photoSpine)" role="img" aria-label="Image of a glowing human spine"/>
    <polygon points="0,40 26,70 0,100" fill="var(--gold)"/>
    <!-- front cover panel -->
    <rect x="380" y="0" width="380" height="520" fill="var(--white)"/>
    <polygon points="560,0 760,0 760,118" fill="var(--gold)"/>
    <polygon points="380,0 480,0 620,300 540,520 380,520" fill="var(--navy)"/>
    <polygon points="480,0 498,0 638,300 620,300" fill="var(--blue)"/>
    <polygon points="642,300 760,245 760,520 562,520" fill="var(--gold)"/>
    <polygon points="512,120 491,156 449,156 428,120 449,84 491,84" fill="url(#photoSkin)" stroke="var(--white)" stroke-width="3" role="img" aria-label="Photo of a chiropractor treating a patient"/>
    <polygon points="574,190 557,219 523,219 506,190 523,161 557,161" fill="url(#photoSkin)" stroke="var(--white)" stroke-width="3" role="img" aria-label="Photo of a neck adjustment"/>
    <polygon points="482,210 467,236 437,236 422,210 437,184 467,184" fill="url(#photoStaff)" stroke="var(--white)" stroke-width="3" role="img" aria-label="Photo of a patient with back pain"/>
  </svg>

  <div class="txt intro">
    <p class="heading">Non-surgical · drug-free</p>
    <p class="heading title">Natural Treatment</p>
    <p class="body-copy">The least invasive treatment for back pain relief. Chiropractic care helps with back pain, neck pain, migraines and posture strain so you can work and live with ease.</p>
  </div>
  <p class="txt hours">Monday – Friday<br>9:00 am – 6:00 pm<br>Saturday by appointment</p>
  <p class="txt address">2480 Harbor Lane, Suite 12<br>Bayview, CA 90000<br>Tel: 555 010 0142</p>

  <div class="txt brand">
    <span class="brand-mark"></span>
    <span class="brand-name">Spine Harbor Chiropractic</span>
  </div>
  <div class="txt tagline">
    <p class="big">We can <b>HELP</b> you</p>
    <p class="small">get out of pain</p>
  </div>
  <p class="txt phone">Tel: 555 010 0142</p>
</section>

<!-- INNER SPREAD -->
<section class="spread spread--inner" aria-label="Brochure inside">
  <svg class="shapes" viewBox="0 0 760 520">
    <defs>
      <linearGradient id="photoBack" x1="0" y1="0" x2="1" y2="1">
        <stop offset="0" stop-color="#f1e4da"/><stop offset="1" stop-color="#b98f78"/>
      </linearGradient>
      <linearGradient id="photoCare" x1="0" y1="0" x2="1" y2="1">
        <stop offset="0" stop-color="#eef3f8"/><stop offset="1" stop-color="#a7bfd6"/>
      </linearGradient>
    </defs>
    <rect x="0" y="0" width="760" height="520" fill="var(--white)"/>
    <polygon points="330,0 640,0 760,90 760,520 240,520" fill="var(--navy)"/>
    <polygon points="312,0 330,0 240,520 222,520" fill="var(--sky)"/>
    <polygon points="640,0 660,0 760,75 760,90" fill="var(--blue)"/>
    <polygon points="380,0 420,0 380,40" fill="var(--blue)"/>
    <!-- left panel photo -->
    <polygon points="235,245 207,293 153,293 125,245 153,197 207,197" fill="url(#photoBack)" stroke="var(--white)" stroke-width="3" role="img" aria-label="Photo of a woman holding her lower back"/>
    <!-- right side photos -->
    <polygon points="400,100 383,129 349,129 332,100 349,71 383,71" fill="url(#photoCare)" stroke="var(--white)" stroke-width="3" role="img" aria-label="Photo of a spinal assessment"/>
    <polygon points="436,150 421,176 391,176 376,150 391,124 421,124" fill="url(#photoBack)" stroke="var(--white)" stroke-width="3" role="img" aria-label="Photo of a shoulder treatment"/>
    <polygon points="640,110 622,141 586,141 568,110 586,79 622,79" fill="url(#photoBack)" stroke="var(--white)" stroke-width="3" role="img" aria-label="Photo of a patient with neck pain"/>
    <polygon points="600,255 583,284 549,284 532,255 549,226 583,226" fill="url(#photoCare)" stroke="var(--white)" stroke-width="3" role="img" aria-label="Photo of a myofascial release session"/>
    <polygon points="520,300 503,329 469,329 452,300 469,271 503,271" fill="url(#photoBack)" stroke="var(--white)" stroke-width="3" role="img" aria-label="Photo of a massage treatment"/>
    <polygon points="690,300 673,329 639,329 622,300 639,271 673,271" fill="url(#photoCare)" stroke="var(--white)" stroke-width="3" role="img" aria-label="Photo of a woman stretching at work"/>
    <polygon points="400,320 383,349 349,349 332,320 349,291 383,291" fill="url(#photoCare)" stroke="var(--white)" stroke-width="3" role="img" aria-label="Photo of a chiropractic adjustment"/>
  </svg>

  <div class="txt policy policy--payment">
    <p class="heading">Payment Policy</p>
    <p class="body-copy on-light">Payment is due at the time of each visit. We accept cash, checks and all major cards. Ask our front desk about package rates and flexible plans for ongoing care.</p>
  </div>
  <div class="txt policy policy--plans">
    <p class="heading">Health Plans</p>
    <p class="body-copy on-light">We work with most insurance plans and will help you check your coverage.</p>
  </div>
  <div class="txt policy policy--questions">
    <p class="heading">Questions?</p>
    <p class="body-copy on-light">Call or visit us any weekday. Our team is happy to help you plan your care.</p>
  </div>
  <div class="txt brand brand--small">
    <span class="brand-mark"></span>
    <span class="brand-name">Spine Harbor Chiropractic</span>
  </div>

  <p class="txt heading service-title svc-spinal">Spinal Curve Correction</p>
  <p class="txt heading service-title svc-myo">Myofascial Release</p>
  <p class="txt heading service-title svc-adjust">Chiropractic<br>Adjustments</p>
  <div class="txt services">
    <p class="heading">Services</p>
    <p class="body-copy">With us you are getting the best treatments and care available</p>
  </div>
</section>

</body>
</html>
```